TUEW - Tally Up Every Week

We need a business card design for a company located in Australia - accounting / tax firm.

2 sided business card - I have attached a one-sided concept that I did in MSWord :) If anything it shows that I want a striking design - bold, fresh and less reserved than your average accounting firm's card.

Rather than having all the info on the front, maybe it could just have name and logo on front?

Want to keep colours in line with logo - orange, black and white.

Happy for full colour. Will be using a matte finish.

About Us (below)
TUEW does business, and more specifically accounting and taxation differently.
People require news and other media at their fingertips so why should business figures and documents be any different?
In combination with Xero, a cloud based accounting package, we store all receipts, tax returns and special documentation with a secure online data-storage provider and provide you with your own login. We are also interested to hear if video conferencing is something you would be interested in.
Using this technology we are able to focus more on your business and less on the data entry.

Target Market(s)

Individual mum and dad clients, and Small to Medium Business

Industry/Entity Type

Accounting

Requirements
Must have
• Must be able to edit the details at a future point in time ie - phone, address, website address, name on card and slogan.

2 sided

Standard Australian business card size
Nice to have
• Rather than having all the info on the front, maybe it could just have name and logo on front?
Should not have
• Don't want "Tally Up Every Week" on the card

```html
<!DOCTYPE html>
<html lang="en">
<head>
<meta charset="utf-8">
<title>TUEW Business Card</title>
<link rel="stylesheet" href="https://fonts.googleapis.com/css2?family=Open+Sans:wght@300;400;700&family=Roboto+Condensed:wght@400&display=swap">
<style>
  :root {
    --canvas: #e9e7e3;
    --card: #0f0f0f;
    --card-edge: #1c1c1c;
    --orange: #e8823f;
    --orange-deep: #d9692a;
    --white: #f4f4f4;
    --grey: #cfcfcf;
  }
  * { box-sizing: border-box; margin: 0; padding: 0; }
  html, body { width: 1200px; height: 1000px; overflow: hidden; }
  body {
    background: var(--canvas);
    font-family: "Open Sans", Arial, sans-serif;
    position: relative;
  }
  .card {
    position: absolute;
    left: 280px;
    width: 640px;
    height: 391px;
    background: linear-gradient(135deg, var(--card-edge), var(--card) 60%);
    overflow: hidden;
    box-shadow: 0 6px 18px rgba(0,0,0,.25);
  }
  .card--front { top: 56px; }
  .card--back { top: 553px; }

  /* front */
  .tab {
    position: absolute;
    right: -20px; top: 34px;
    width: 70px; height: 62px;
    background: var(--orange);
    border-radius: 16px;
  }
  .brand {
    position: absolute;
    left: 52px; top: 96px;
    display: flex; align-items: center;
  }
  .brand__mark {
    width: 104px; height: 104px;
    border-radius: 50%;
    background: var(--orange);
    flex: none;
    margin-right: 12px;
  }
  .brand__name {
    font-weight: 300;
    font-size: 104px;
    line-height: 1;
    color: var(--white);
    letter-spacing: 2px;
  }
  .tagline {
    position: absolute;
    left: 170px; top: 212px;
    font-size: 13px;
    color: var(--grey);
    letter-spacing: .2px;
  }
  .tagline .dot {
    display: inline-block;
    width: 7px; height: 7px;
    border-radius: 50%;
    background: var(--white);
    margin: 0 4px 1px;
  }
  .holder {
    position: absolute;
    left: 44px; bottom: 44px;
    display: flex; align-items: baseline;
    color: var(--white);
  }
  .holder__name {
    font-weight: 700;
    font-size: 32px;
    letter-spacing: -.5px;
  }
  .holder__role {
    font-family: "Roboto Condensed", "Arial Narrow", sans-serif;
    font-size: 17px;
    margin-left: 6px;
  }
  .rule {
    position: absolute;
    left: 330px; right: 0; bottom: 78px;
    height: 2px;
    background: var(--white);
  }

  /* back */
  .bar-long {
    position: absolute;
    left: 340px; right: 0; top: 120px;
    height: 66px;
    background: var(--orange-deep);
  }
  .bar-short {
    position: absolute;
    left: 0; top: 160px;
    width: 48px; height: 80px;
    background: var(--orange-deep);
  }
  .contacts {
    position: absolute;
    left: 66px; top: 142px;
    list-style: none;
  }
  .contacts li {
    display: flex; align-items: center;
    font-size: 25px;
    color: var(--white);
    height: 38px;
  }
  .contacts svg {
    width: 28px; height: 28px;
    margin-right: 10px;
    flex: none;
  }
</style>
</head>
<body>

<section class="card card--front" aria-label="Card front">
  <div class="tab"></div>
  <div class="brand">
    <div class="brand__mark"></div>
    <div class="brand__name">TUEW</div>
  </div>
  <p class="tagline">Bookkeeping<span class="dot"></span>Accounting<span class="dot"></span>Taxation</p>
  <div class="rule"></div>
  <div class="holder">
    <span class="holder__name">Daniel Reed</span>
    <span class="holder__role">Tax Agent</span>
  </div>
</section>

<section class="card card--back" aria-label="Card back">
  <div class="bar-long"></div>
  <div class="bar-short"></div>
  <ul class="contacts">
    <li>
      <svg viewBox="0 0 28 28" aria-hidden="true"><rect x="2" y="7" width="24" height="15" fill="#f4f4f4"/><path d="M2 7 L14 16 L26 7" fill="none" stroke="#0f0f0f" stroke-width="2"/></svg>
      reed@tuew.com.au
    </li>
    <li>
      <svg viewBox="0 0 28 28" aria-hidden="true"><rect x="8" y="3" width="13" height="22" rx="2.5" fill="none" stroke="#f4f4f4" stroke-width="2"/><line x1="12" y1="21" x2="17" y2="21" stroke="#f4f4f4" stroke-width="1.5"/></svg>
      0400 123 456
    </li>
    <li>
      <svg viewBox="0 0 28 28" aria-hidden="true"><circle cx="14" cy="14" r="11" fill="#f4f4f4"/><ellipse cx="14" cy="14" rx="5" ry="11" fill="none" stroke="#0f0f0f" stroke-width="1.5"/><line x1="3" y1="14" x2="25" y2="14" stroke="#0f0f0f" stroke-width="1.5"/></svg>
      www.tuew.com.au
    </li>
  </ul>
</section>

</body>
</html>
```